Alapca breeding needs a website

Presentation of the farm, animals (stallions, mares, information about the animals, for sale) and possible later expansion with a webshop (alpaca wool products). We want to present our farm and the animals on the farm on this page. A mission why we are doing this. Furthermore, each animal should be shown with a picture and described. Later we want to sell our own products made from alpaca wool via a webshop. But we still need to grow a bit to do that.

Target Market(s)

Information about my alpaca breeding and the alpaca farm

Industry/Entity Type

Tierzucht

Number of Pages Required

1 page

Font styles to use
Sans Serif

Requirements
Must have
• Modern design that matches the logo
Nice to have
• Intuitive operation / Clear structure
Should not have
• No

```html
<!DOCTYPE html>
<html lang="en">
<head>
<meta charset="UTF-8">
<title>Meadowcrest Alpacas</title>
<link href="https://fonts.googleapis.com/css2?family=Cinzel:wght@500;600&family=Montserrat:wght@400;500;600&family=Poppins:wght@300;400;500;600&display=swap" rel="stylesheet">
<style>
:root{
  --green:#7cc043;
  --navy:#1b2a4a;
  --text:#555a63;
  --light:#f7f5f6;
  --white:#ffffff;
  --line:#d7d7d7;
}
*{margin:0;padding:0;box-sizing:border-box}
html,body{width:1200px;height:4549px;overflow:hidden}
body{position:relative;background:var(--white);font-family:'Poppins',sans-serif;color:var(--text)}
.abs{position:absolute}
.serif{font-family:'Cinzel',serif;font-weight:500;color:var(--navy)}
.btn{position:absolute;display:flex;align-items:center;justify-content:center;border-radius:40px;background:var(--green);color:var(--white);font-family:'Montserrat',sans-serif;font-weight:600;font-size:18px;letter-spacing:.3px}
.eyebrow{position:absolute;left:0;width:1200px;text-align:center;color:var(--green);font-size:19px}

/* header */
.header{left:0;top:0;width:1200px;height:116px;background:var(--white)}
.brand-badge{left:92px;top:-20px;width:214px;height:218px;border-radius:50%;background:var(--white);z-index:3;display:flex;align-items:flex-end;justify-content:center;padding-bottom:60px}
.brand-name{font-family:'Montserrat',sans-serif;font-weight:600;font-size:22px;line-height:28px;color:var(--navy);text-align:center}
.topline{right:111px;top:16px;font-family:'Montserrat',sans-serif;font-weight:600;font-size:17px;color:var(--navy);display:flex;gap:12px;align-items:center}
.topline svg{vertical-align:-2px;margin-right:5px}
.nav{right:111px;top:60px;display:flex;gap:29px;align-items:center;font-family:'Montserrat',sans-serif;font-weight:600;font-size:17px;color:var(--navy)}
.nav .active{color:var(--green)}
.nav .shop{background:var(--green);color:var(--white);padding:10px 22px;border-radius:30px}

/* hero */
.hero{left:0;top:116px;width:1200px;height:599px;background:linear-gradient(180deg,#3a8fc4 0%,#6fa3bf 30%,#6a6a62 55%,#8a6f45 75%,#b08a4e 100%)}
.hero-title{left:111px;top:258px;font-size:56px;line-height:66px;color:var(--white)}
.hero-sub{left:111px;top:408px;font-size:20px;color:var(--white)}
.hero-btn{left:111px;top:468px;width:215px;height:65px;background:var(--white);color:var(--navy)}

/* about */
.about-eyebrow{left:111px;top:846px;color:var(--green);font-size:19px}
.about-title{left:111px;top:896px;font-size:39px;line-height:52px}
.about-text{left:611px;top:834px;width:480px;font-size:16px;line-height:28.5px}
.about-btn{left:609px;top:1008px;width:153px;height:58px}

/* animals */
.animals{left:0;top:1149px;width:1200px;height:1963px;background:var(--light)}
.section-title{position:absolute;left:0;width:1200px;text-align:center;font-size:38px}
.card{position:absolute;width:311px}
.card-photo{width:311px;height:310px}
.card-name{margin-top:30px;font-family:'Montserrat',sans-serif;font-weight:600;font-size:25px;color:var(--navy);white-space:nowrap}
.card-desc{margin-top:13px;font-size:16px;line-height:27.5px}
.view-btn{left:522px;top:2951px;width:156px;height:58px}

/* cta */
.cta{left:0;top:3112px;width:1200px;height:498px;background:linear-gradient(180deg,#6e7a6c 0%,#5c7a46 35%,#5e8a3a 70%,#6b9140 100%)}
.cta-title{left:0;top:3196px;width:1200px;text-align:center;font-size:38px;color:var(--white)}
.cta-text{left:195px;top:3274px;width:810px;text-align:center;font-size:16px;line-height:29px;color:var(--white)}
.cta-btn{left:514px;top:3405px;width:172px;height:58px}

/* subscribe */
.subscribe{left:0;top:3610px;width:1200px;height:374px;background:var(--light)}
.form{left:173px;top:3825px;width:854px;height:75px;border:1px solid var(--green);background:var(--white);display:flex}
.form .field{flex:1;display:flex;align-items:center;padding-left:25px;font-size:17px;color:#4a4f58}
.form .submit{width:134px;background:var(--green);color:var(--white);display:flex;align-items:center;justify-content:center;font-family:'Montserrat',sans-serif;font-weight:600;font-size:18px}

/* footer */
.footer-links{left:184px;top:4096px;list-style:none;font-family:'Montserrat',sans-serif;font-weight:500;font-size:17px;color:var(--navy);line-height:33.5px}
.footer-brand{left:420px;top:4040px;width:360px;display:flex;flex-direction:column;align-items:center;gap:22px}
.footer-brand .mark{width:120px;height:120px;border-radius:50%;background:var(--green)}
.footer-brand .name{font-family:'Montserrat',sans-serif;font-weight:600;font-size:34px;line-height:42px;color:var(--navy);text-align:center}
.contact-head{left:798px;top:4090px;font-family:'Montserrat',sans-serif;font-weight:600;font-size:18px;color:var(--navy)}
.contact-item{position:absolute;left:798px;display:flex;align-items:center;gap:18px;font-size:16px;line-height:26px;color:var(--navy)}
.icon-ring{width:42px;height:42px;border:1px solid #bbb;border-radius:50%;display:flex;align-items:center;justify-content:center;flex:none}
.divider{left:111px;top:4372px;width:978px;height:1px;background:#9a9a9a}
.copyright{left:106px;top:4400px;font-size:16px;color:var(--navy)}
.social{left:937px;top:4388px;display:flex;gap:6px}
.social span{width:46px;height:46px;border:1px solid #b9b9b9;border-radius:50%;display:flex;align-items:center;justify-content:center}
.social span::after{content:"";width:12px;height:12px;border-radius:50%;background:var(--green)}
.fence{left:0;top:4448px;width:1200px;height:101px;background:linear-gradient(180deg,rgba(235,235,235,0) 0%,#ececec 55%,#e6e6e6 100%)}
</style>
</head>
<body>

<header class="abs header"></header>
<div class="abs brand-badge"><div class="brand-name">Meadowcrest<br>Alpacas</div></div>
<div class="abs topline">
  <span><svg width="15" height="15" viewBox="0 0 24 24"><path fill="var(--green)" d="M6.6 10.8a15.1 15.1 0 0 0 6.6 6.6l2.2-2.2c.3-.3.7-.4 1-.2 1.1.4 2.3.6 3.6.6.6 0 1 .4 1 1V20c0 .6-.4 1-1 1A17 17 0 0 1 3 4c0-.6.4-1 1-1h3.5c.6 0 1 .4 1 1 0 1.3.2 2.5.6 3.6.1.3 0 .7-.2 1z"/></svg>1 555 010 2040</span>
  <span>|</span>
  <span><svg width="16" height="13" viewBox="0 0 24 18"><rect width="24" height="18" rx="2" fill="var(--green)"/><path d="M2 3l10 7 10-7" stroke="#fff" stroke-width="2" fill="none"/></svg>info@meadowcrestalpacas.com</span>
</div>
<nav class="abs nav">
  <span class="active">Home</span><span>Who We Are?</span><span>Breeding</span><span>Contact Us</span><span class="shop">SHOP</span>
</nav>

<section class="abs hero" role="img" aria-label="Photo of two white alpacas standing in golden grassland before a mountain under blue sky"></section>
<h1 class="abs serif hero-title">MEADOWCREST<br>ALPACAS</h1>
<p class="abs hero-sub">Duis aute irure dolor in reprehenderit in volu</p>
<div class="btn hero-btn">GET MORE INFO</div>

<p class="abs about-eyebrow">who We Are</p>
<h2 class="abs serif about-title">WELCOME TO<br>MEADOWCREST<br>ALPACAS</h2>
<p class="abs about-text">Nemo enim ipsam voluptatem quia voluptas sit aspernatur aut odit aut fugit, sed quia consequuntur magni dolores os qui ratione voluptatem sequi nesciunt. Neque porro quisqa mest, qui dolorem ipsum quia dolor sit amet, consecte jiliur, adipisci velit tempora incidunt ut labor.</p>
<div class="btn about-btn">READ MORE</div>

<section class="abs animals"></section>
<p class="eyebrow" style="top:1230px">Breeding</p>
<h2 class="serif section-title" style="top:1280px">MEET THE ANIMALS</h2>

<div class="card" style="left:111px;top:1377px"><div class="card-photo" role="img" aria-label="Photo of two alpacas, brown and cream" style="background:linear-gradient(135deg,#8a6a45,#c9b28e)"></div><h3 class="card-name">Finibus Bonoruet Malor</h3><p class="card-desc">Nemo enim ipsam voluptatem quia voluptas sit aspern atur aut odit aut fugit, sed quia conseq.</p></div>
<div class="card" style="left:445px;top:1377px"><div class="card-photo" role="img" aria-label="Photo of two horses looking out of a stable" style="background:linear-gradient(135deg,#7aa88a,#6b3f24)"></div><h3 class="card-name">Finibus Bonoruet Malor</h3><p class="card-desc">Nemo enim ipsam voluptatem quia voluptas sit aspern atur aut odit aut fugit, sed quia conseq.</p></div>
<div class="card" style="left:778px;top:1377px"><div class="card-photo" role="img" aria-label="Photo of white alpacas on a field under cloudy sky" style="background:linear-gradient(180deg,#7d9fc4,#d8d6d0 55%,#8c7856)"></div><h3 class="card-name">Finibus Bonoruet Malor</h3><p class="card-desc">Nemo enim ipsam voluptatem quia voluptas sit aspern atur aut odit aut fugit, sed quia conseq.</p></div>

<div class="card" style="left:111px;top:1900px"><div class="card-photo" role="img" aria-label="Photo of a person stroking a white alpaca" style="background:linear-gradient(135deg,#a8a497,#d9d2c2 50%,#6b4b3a)"></div><h3 class="card-name">Finibus Bonoruet Malor</h3><p class="card-desc">Nemo enim ipsam voluptatem quia voluptas sit aspern atur aut odit aut fugit, sed quia conseq.</p></div>
<div class="card" style="left:445px;top:1900px"><div class="card-photo" role="img" aria-label="Photo of a brown alpaca eating hay" style="background:linear-gradient(135deg,#5b4330,#a78560)"></div><h3 class="card-name">Finibus Bonoruet Malor</h3><p class="card-desc">Nemo enim ipsam voluptatem quia voluptas sit aspern atur aut odit aut fugit, sed quia conseq.</p></div>
<div class="card" style="left:778px;top:1900px"><div class="card-photo" role="img" aria-label="Photo of a white horse wearing a grey blanket" style="background:linear-gradient(135deg,#8c6a3e,#e2ddd5 55%,#9a9a9c)"></div><h3 class="card-name">Finibus Bonoruet Malor</h3><p class="card-desc">Nemo enim ipsam voluptatem quia voluptas sit aspern atur aut odit aut fugit, sed quia conseq.</p></div>

<div class="card" style="left:111px;top:2423px"><div class="card-photo" role="img" aria-label="Photo of a brown and white pony with a colourful halter" style="background:linear-gradient(135deg,#6f8a3e,#a0521f 55%,#e8d8c6)"></div><h3 class="card-name">Finibus Bonoruet Malor</h3><p class="card-desc">Nemo enim ipsam voluptatem quia voluptas sit aspern atur aut odit aut fugit, sed quia conseq.</p></div>
<div class="card" style="left:445px;top:2423px"><div class="card-photo" role="img" aria-label="Photo of a fluffy cream alpaca in a dry paddock" style="background:linear-gradient(180deg,#8fa6b4,#c6a578 40%,#e3d3bc)"></div><h3 class="card-name">Finibus Bonoruet Malor</h3><p class="card-desc">Nemo enim ipsam voluptatem quia voluptas sit aspern atur aut odit aut fugit, sed quia conseq.</p></div>
<div class="card" style="left:778px;top:2423px"><div class="card-photo" role="img" aria-label="Photo of a chestnut horse in a green meadow" style="background:linear-gradient(135deg,#3f6b2a,#9c5a2a 50%,#7fa64a)"></div><h3 class="card-name">Finibus Bonoruet Malor</h3><p class="card-desc">Nemo enim ipsam voluptatem quia voluptas sit aspern atur aut odit aut fugit, sed quia conseq.</p></div>

<div class="btn view-btn">VIEW MORE</div>

<section class="abs cta" role="img" aria-label="Photo of a herd of alpacas grazing on a green mountain valley with a red-roofed barn"></section>
<h2 class="abs serif cta-title">THINKING OF BUYING AN BREED?</h2>
<p class="abs cta-text">Neque porro quisquam est, qui dolorem ipsum quia dolor sit amet, consectetur, adipisci velit, sed quia non numquam eius modi tempora incidunt ut labore et dolore magnam aliquam quaerat vo luptatem. Ut enim ad minima veniam, quis nostrum exercitationem.</p>
<div class="btn cta-btn">CONTACT US</div>

<section class="abs subscribe"></section>
<p class="eyebrow" style="top:3677px">Subscribe</p>
<h2 class="serif section-title" style="top:3728px">JOIN THE MEADOWCREST ALPACAS FAMILY!</h2>
<div class="abs form"><div class="field">Email Address</div><div class="submit">SUBMIT</div></div>

<ul class="abs footer-links"><li>Home</li><li>Who We Are?</li><li>Breeding</li><li>Contact Us</li><li>TERMS</li><li>SITE MAP</li></ul>
<div class="abs footer-brand"><span class="mark"></span><span class="name">Meadowcrest<br>Alpacas</span></div>
<p class="abs contact-head">Contact Information</p>
<div class="contact-item" style="top:4142px"><span class="icon-ring"><svg width="14" height="18" viewBox="0 0 14 20"><path d="M7 1a6 6 0 0 0-6 6c0 4.5 6 12 6 12s6-7.5 6-12a6 6 0 0 0-6-6z" fill="none" stroke="var(--green)" stroke-width="1.6"/><circle cx="7" cy="7" r="2" fill="var(--green)"/></svg></span><span>No 1234 Fern Hollow Road,<br>Cedar Falls, Oregon</span></div>
<div class="contact-item" style="top:4208px"><span class="icon-ring"><svg width="16" height="16" viewBox="0 0 24 24"><path fill="var(--green)" d="M6.6 10.8a15.1 15.1 0 0 0 6.6 6.6l2.2-2.2c.3-.3.7-.4 1-.2 1.1.4 2.3.6 3.6.6.6 0 1 .4 1 1V20c0 .6-.4 1-1 1A17 17 0 0 1 3 4c0-.6.4-1 1-1h3.5c.6 0 1 .4 1 1 0 1.3.2 2.5.6 3.6.1.3 0 .7-.2 1z"/></svg></span><span>1 555 010 2040</span></div>
<div class="contact-item" style="top:4261px"><span class="icon-ring"><svg width="17" height="13" viewBox="0 0 24 18"><rect width="24" height="18" rx="2" fill="var(--green)"/><path d="M2 3l10 7 10-7" stroke="#fff" stroke-width="2" fill="none"/></svg></span><span>info@meadowcrestalpacas.com</span></div>

<div class="abs divider"></div>
<p class="abs copyright">© Copyright 2024, Meadowcrest Alpacas. All Rights Reserved</p>
<div class="abs social" aria-label="Social media links"><span></span><span></span><span></span></div>
<div class="abs fence" role="img" aria-label="Faint illustration of a white picket fence with flowers"></div>

</body>
</html>
```